Functional Beverage- Flavoured Vitamin Water

Hi,

We need a product label design for a new flavoured vitamin water in London: "Lumo Brisk" .

Lumo Brisk is a refreshing vitamin infusion ready to drink beverage. It is a naturally sweetened (low sugar NOT no sugar, but free from artificial sweetners), with natural colours and flavours - with added vitamins and supplements, including natural botanicals. We want to clearly label this to be a health drink and highlight the benefits. It is a STILL drink and either CLEAR or TINTED RED depending on the flavour.

We have used leading research from the nutritional industry to create functional blends in a light refreshing water that is not sugar laden or artificially flavoured. WE TASTE GREAT!

These are the 4 flavours however for the purposes of the brief I am happy for the designers to focus on either

1. CRANBERRY RASPERRY - rose red - REDOX (contains antioxidants and help immunity)
2. COCONUT PINEAPPLE - clear - BEAUTY (helps maintain hair, skin and nails)

I want the product label to be fresh and stand out as this will be facing competition from established brands (Trevanne / K-Drink).

Labels will be printed on self-adhesive plastic and be applied to a 500 ml PET clear plastic bottle. The label itself would be no more than 190mm wide by 80mm tall and will be a rectangle (to give you an idea of scale when the consumer looks at the label).

I want something as striking, pure and playful as these two brands have on their waters (but not as minimal...)

1. http://thewanderingowl.example/?p=48113
2. http://www.pelmorstudio.example/energy/arch/007215.php
3. Existing bottle is here: https://files.example/QmXpWs83

We will be relying on social media for marketing and PR so fthe design needs to transfer to that type of media well.

Thanks and good luck
Updates

Hi all,

Just a note to the invited designers - hoping some more of you can jump into the project over the weekend if you have not already submitted designs.

Thanks and regards,

Tom

Reason: Extending so we can get some more designs submitted. Thanks.

Hi,

I have increased the budget to allow for a $100 2nd prize, as we are seeing some strong designs in the closing stages.

Regards,
Tom

Reason: Collating final feedback on submissions.

Target Market(s)

18-35 yeare old professionals who consume vitamin supplements and want a ready to drink flavoured water that's different to the standard offering.

It is unisex but feel the brand may appeal more to women initially. But I dont want to disenfranchise men.

Industry/Entity Type

Marketing

Requirements
Must have
• Health benefit claims
Flavour names
Mention the natural fruit sugars and stevia
Nice to have
• Mention how it's "Low Cal not No Cal"

I like the idea of a clear or semi clear label that uses the back of the label on the opposite side like the OKRA water bottle in the attached file. This makes it looks so much more 3d than a "front" label... not a mandatory requirement - just an idea to think of.

```html
<!DOCTYPE html>
<html lang="en">
<head>
<meta charset="utf-8">
<title>Lumo Brisk – Vitamin Water Labels</title>
<link rel="stylesheet" href="https://fonts.googleapis.com/css2?family=Raleway:wght@300;400;600&display=swap">
<style>
  :root {
    --canvas: #ffffff;
    --label-light: #fbfafc;
    --label-shade: #eceaef;
    --brand-blue: #1ea2dc;
    --redox-pink: #e8306f;
    --beauty-gold: #f4c443;
    --claim-grey: #6b6b70;
  }

  html, body {
    margin: 0;
    padding: 0;
    width: 1200px;
    height: 1000px;
    overflow: hidden;
    background: var(--canvas);
  }

  .range {
    position: relative;
    width: 1200px;
    height: 1000px;
    display: flex;
    justify-content: center;
    align-items: center;
    gap: 100px;
  }

  .label {
    position: relative;
    width: 350px;
    height: 480px;
    background: linear-gradient(90deg, var(--label-shade) 0%, var(--label-light) 25%, var(--label-light) 70%, var(--label-shade) 100%);
    font-family: "Raleway", sans-serif;
    box-sizing: border-box;
  }

  .label--redox { --flavour: var(--redox-pink); }
  .label--beauty { --flavour: var(--beauty-gold); }

  .brand {
    position: absolute;
    left: 22px;
    top: 82px;
    width: 299px;
    height: 120px;
  }

  .brand__dot {
    position: absolute;
    left: 0;
    top: 4px;
    width: 112px;
    height: 112px;
    border-radius: 50%;
    background: var(--flavour);
  }

  .brand__name {
    position: absolute;
    right: 0;
    top: 14px;
    margin: 0;
    font-weight: 600;
    font-size: 44px;
    line-height: 46px;
    letter-spacing: 2px;
    color: var(--brand-blue);
    text-transform: uppercase;
    text-align: right;
  }

  .brand__rule {
    position: absolute;
    left: 22px;
    top: 219px;
    width: 299px;
    height: 3px;
    background: var(--brand-blue);
    border-radius: 2px;
  }

  .flavour {
    position: absolute;
    left: 22px;
    right: 22px;
    top: 236px;
    margin: 0;
    font-weight: 300;
    font-size: 57px;
    line-height: 60px;
    letter-spacing: -0.5px;
    color: var(--flavour);
    text-align: right;
  }

  .benefit {
    position: absolute;
    left: 14px;
    right: 22px;
    top: 362px;
    margin: 0;
    font-weight: 400;
    font-size: 16px;
    color: var(--claim-grey);
    text-align: right;
    white-space: nowrap;
  }

  .label--redox .benefit strong {
    font-weight: 400;
  }

  .facts {
    position: absolute;
    left: 38px;
    right: 28px;
    top: 406px;
    display: flex;
    justify-content: space-between;
    font-size: 15px;
    font-weight: 400;
    color: var(--brand-blue);
  }
</style>
</head>
<body>
  <main class="range">

    <section class="label label--redox">
      <div class="brand">
        <span class="brand__dot"></span>
        <h1 class="brand__name">Lumo<br>Brisk</h1>
      </div>
      <div class="brand__rule"></div>
      <h2 class="flavour">Cranberry<br>Raspberry</h2>
      <p class="benefit">antioxidants and help immunity</p>
      <div class="facts">
        <span class="facts__calorie">Low Calorie</span>
        <span class="facts__volume">500 mL</span>
      </div>
    </section>

    <section class="label label--beauty">
      <div class="brand">
        <span class="brand__dot"></span>
        <h1 class="brand__name">Lumo<br>Brisk</h1>
      </div>
      <div class="brand__rule"></div>
      <h2 class="flavour">Coconut<br>Pineapple</h2>
      <p class="benefit">helps maintain hair, skin &amp; nails</p>
      <div class="facts">
        <span class="facts__calorie">Low Calorie</span>
        <span class="facts__volume">500 mL</span>
      </div>
    </section>

  </main>
</body>
</html>
```